Halvyne System Web Page Design

This project is to design 6 pages of a web based medical system for clinics, hospitals, drugs suppliers, general items suppliers, insurance company, laboratories and patients (basically all parties which could be involved in).We want the designs of the browser, button, icon and layout are based on Vex, which is user friendly, looks professional, simple and neat but with powerful functions. We have uploaded few pictures of another system, please do not copy its design because this is not what we are looking for, the pictures are for you to know the elements should be included in our pages. Halvyne web-base system, design 6 pages1. Login PageShould include the following elements-company id with input field-login id with input field-password with input field2. Main Page (Navigation page)Should include the following elements-Appointment-Consultation-Patient-Drugs inventory -General supplies inventory -Laboratory-Suppliers-Insurance-Reports 3. Appointment PageShould include all the the elements in the respective pictures plus the followings-Daily View, Weekly View, Monthly View buttons4. Consultation PageShould include all the the elements in the respective picture5. Patient Page5.1 General information Should include all the the elements in the respective picture5.2 medical history/lab reportsShould include all the the elements in the respective picture plus the followings-Notify patient button-Share report button.
Updated on 28 Nov:
Please stop using Ward Keystone in your designs which is not the name of our system. We have just rename our system to Halvyne, please take note.
We need the system to look professional not playful, do not use too many colors and playful icons.
professional users

```html
<!DOCTYPE html>
<html lang="en">
<head>
<meta charset="utf-8">
<title>Halvyne – Patient</title>
<link href="https://fonts.googleapis.com/css2?family=Roboto:wght@300;400;500;700&family=Roboto+Condensed:wght@400;700&display=swap" rel="stylesheet">
<style>
  :root{
    --brand:#0b5275;
    --sidebar:#eeeeee;
    --page:#f4f4f4;
    --panel:#ffffff;
    --ink:#111111;
    --muted:#333333;
    --line:#d8d8d8;
    --field-line:#cfcfcf;
    --arrow-bg:#f0f0f0;
    --arrow:#c4c4c4;
  }
  *{box-sizing:border-box;margin:0;padding:0}
  html,body{width:1028px;height:1200px;overflow:hidden;background:var(--page)}
  .stage{position:absolute;left:0;top:0;width:1366px;height:1595px;transform:scale(0.75256);transform-origin:0 0;background:var(--page);font-family:'Roboto',sans-serif;color:var(--ink)}

  .sidebar{position:absolute;left:0;top:0;width:184px;height:1595px;background:var(--sidebar)}
  .brand{height:72px;text-align:right;padding-right:17px;padding-top:22px;font:400 25px 'Roboto',sans-serif;color:var(--brand)}
  .nav{list-style:none;border-top:1px solid var(--line)}
  .nav li{height:49px;border-bottom:1px solid var(--line);text-align:right;padding-right:24px;display:flex;align-items:center;justify-content:flex-end;font:400 12.5px 'Roboto Condensed',sans-serif;color:var(--ink);position:relative}
  .nav li.is-active{background:var(--page);color:var(--brand)}
  .nav li.is-active::before{content:"";position:absolute;left:0;top:0;bottom:0;width:4px;background:var(--brand)}

  .account{position:absolute;right:40px;top:14px;font:400 10px 'Roboto Condensed',sans-serif;color:var(--muted)}
  .account span{margin:0 6px}
  .page-title{position:absolute;left:224px;top:62px;font:300 32px 'Roboto',sans-serif;letter-spacing:.5px;color:var(--ink)}
  .btn-new{position:absolute;left:1197px;top:58px;width:129px;height:40px;background:var(--brand);color:#fff;border-radius:3px;display:flex;align-items:center;justify-content:center;gap:4px;font:700 13px 'Roboto Condensed',sans-serif}

  .panel{position:absolute;left:224px;top:114px;width:1102px;height:1406px;background:var(--panel);padding:0 24px}
  .stats{height:49px;border-bottom:1px solid var(--ink);display:flex;justify-content:flex-end;align-items:center;padding-top:8px;font:400 12px 'Roboto Condensed',sans-serif;color:var(--ink)}
  .stats .sep{margin:0 12px}

  .form{display:grid;grid-template-columns:519px 519px;column-gap:16px;row-gap:21px;margin-top:46px}
  .pair{display:flex;gap:8px}
  .pair .field{flex:1}
  .label{display:block;font:700 12.5px 'Roboto',sans-serif;line-height:13px;margin-bottom:6px;letter-spacing:.1px}
  .input{height:40px;border:1px solid var(--field-line);background:#fff;display:flex;align-items:center;padding:0 8px;font:400 16px 'Roboto',sans-serif;color:#222;position:relative}
  .area{height:120px;border:1px solid var(--field-line);background:#fff}
  .select::after{content:"";position:absolute;right:4px;top:4px;width:30px;height:30px;background:var(--arrow-bg)}
  .select svg{position:absolute;right:11px;top:15px;z-index:1}
  .radios{height:40px;display:flex;align-items:center;gap:22px;padding-left:16px;font:400 16px 'Roboto',sans-serif;color:var(--muted)}
  .radio{display:flex;align-items:center;gap:6px}
  .dot{width:19px;height:19px;border:1px solid var(--field-line);border-radius:50%;display:flex;align-items:center;justify-content:center}
  .dot.on::after{content:"";width:9px;height:9px;border-radius:50%;background:var(--brand)}
  .add-group{display:flex;justify-content:flex-end;align-items:center;gap:4px;margin-top:14px;font:700 12.5px 'Roboto Condensed',sans-serif;color:var(--brand)}

  .actions{position:absolute;left:0;right:0;top:1334px;display:flex;justify-content:center;gap:8px}
  .btn{width:160px;height:48px;border:1px solid var(--brand);border-radius:2px;display:flex;align-items:center;justify-content:center;font:700 16px 'Roboto Condensed',sans-serif;color:var(--brand);background:#fff}
  .btn.primary{background:var(--brand);color:#fff}

  .footer{position:absolute;left:184px;right:0;top:1566px;text-align:center;font:400 10px 'Roboto Condensed',sans-serif;color:var(--muted)}
  .footer span{margin:0 6px}
</style>
</head>
<body>
<div class="stage">
  <aside class="sidebar">
    <div class="brand">Halvyne</div>
    <ul class="nav">
      <li>Home</li>
      <li>Appointment</li>
      <li>Consultation</li>
      <li class="is-active">Patient</li>
      <li>Drugs Inventory</li>
      <li>General Supplies Inventory</li>
      <li>Laboratory</li>
      <li>Suppliers</li>
      <li>Insurance</li>
      <li>Reports</li>
    </ul>
  </aside>

  <div class="account">Company/Username<span>|</span>Logout</div>
  <h1 class="page-title">PATIENT</h1>
  <div class="btn-new">
    <svg width="12" height="12" viewBox="0 0 12 12"><path d="M6 0v12M0 6h12" stroke="#fff" stroke-width="2"/></svg>
    NEW PATIENT
  </div>

  <main class="panel">
    <div class="stats">No. of Records:&nbsp; 4912<span class="sep">|</span>Last Patient Code:&nbsp; 021010<span class="sep">|</span>Last Modify Date:&nbsp; n/a</div>

    <div class="form">
      <div class="pair">
        <div class="field"><span class="label">PATIERNT CODE</span><div class="input">0201010</div></div>
        <div class="field"><span class="label">PREFIX</span><div class="input select"><svg width="14" height="8" viewBox="0 0 14 8"><path d="M1 1l6 5 6-5" fill="none" stroke="var(--arrow)" stroke-width="2"/></svg></div></div>
      </div>
      <div class="field"><span class="label">GENDER</span>
        <div class="radios"><span class="radio"><span class="dot on"></span>Male</span><span class="radio"><span class="dot"></span>Female</span></div>
      </div>

      <div class="field"><span class="label">ENGLISH NAME</span><div class="input"></div></div>
      <div class="field"><span class="label">CHINESE NAME</span><div class="input"></div></div>

      <div class="field"><span class="label">H.K.I.D</span><div class="input"></div></div>
      <div class="pair">
        <div class="field"><span class="label">D.O.B (DD/MM/CCYY)</span><div class="input"></div></div>
        <div class="field"><span class="label">BLOOD TYPE</span><div class="input select"><svg width="14" height="8" viewBox="0 0 14 8"><path d="M1 1l6 5 6-5" fill="none" stroke="var(--arrow)" stroke-width="2"/></svg></div></div>
      </div>

      <div class="field"><span class="label">MOBILE NO.</span><div class="input"></div></div>
      <div class="field"><span class="label">TEL</span><div class="input"></div></div>

      <div class="field"><span class="label">RES. ADDRESS</span><div class="area"></div></div>
      <div class="field"><span class="label">BUS. ADDRESS</span><div class="area"></div></div>

      <div class="field"><span class="label">RES. DISTRICT</span><div class="input select"><svg width="14" height="8" viewBox="0 0 14 8"><path d="M1 1l6 5 6-5" fill="none" stroke="var(--arrow)" stroke-width="2"/></svg></div></div>
      <div class="field"><span class="label">BUS. DISTRICT</span><div class="input select"><svg width="14" height="8" viewBox="0 0 14 8"><path d="M1 1l6 5 6-5" fill="none" stroke="var(--arrow)" stroke-width="2"/></svg></div></div>

      <div class="field"><span class="label">RES. AREA</span><div class="input select"><svg width="14" height="8" viewBox="0 0 14 8"><path d="M1 1l6 5 6-5" fill="none" stroke="var(--arrow)" stroke-width="2"/></svg></div></div>
      <div class="field"><span class="label">BUS. AREA</span><div class="input select"><svg width="14" height="8" viewBox="0 0 14 8"><path d="M1 1l6 5 6-5" fill="none" stroke="var(--arrow)" stroke-width="2"/></svg></div></div>

      <div class="field"><span class="label">OCCUPATION</span><div class="input select"><svg width="14" height="8" viewBox="0 0 14 8"><path d="M1 1l6 5 6-5" fill="none" stroke="var(--arrow)" stroke-width="2"/></svg></div></div>
      <div class="field"><span class="label">DR. IN CHARGE</span><div class="input select"><svg width="14" height="8" viewBox="0 0 14 8"><path d="M1 1l6 5 6-5" fill="none" stroke="var(--arrow)" stroke-width="2"/></svg></div></div>

      <div class="field"><span class="label">CONTACT</span><div class="input select"><svg width="14" height="8" viewBox="0 0 14 8"><path d="M1 1l6 5 6-5" fill="none" stroke="var(--arrow)" stroke-width="2"/></svg></div></div>
      <div class="field"><span class="label">REFERRED BY</span><div class="input select"><svg width="14" height="8" viewBox="0 0 14 8"><path d="M1 1l6 5 6-5" fill="none" stroke="var(--arrow)" stroke-width="2"/></svg></div></div>

      <div class="field"><span class="label">INSURANCE NO.</span><div class="input"></div></div>
      <div class="field"><span class="label">EMAIL</span><div class="input"></div></div>

      <div class="field"><span class="label">INSURANCE PLAN</span><div class="area"></div></div>
      <div class="field"><span class="label">FAMILY HISTORY</span><div class="area"></div></div>

      <div class="field"><span class="label">REMAKR</span><div class="area"></div></div>
      <div class="field"><span class="label">GROUP</span><div class="input select"><svg width="14" height="8" viewBox="0 0 14 8"><path d="M1 1l6 5 6-5" fill="none" stroke="var(--arrow)" stroke-width="2"/></svg></div>
        <div class="add-group"><svg width="11" height="11" viewBox="0 0 11 11"><path d="M5.5 0v11M0 5.5h11" stroke="var(--brand)" stroke-width="2"/></svg>ADD GROUP</div>
      </div>
    </div>

    <div class="actions">
      <div class="btn primary">SAVE</div>
      <div class="btn">Print Eng.</div>
      <div class="btn">Print Chi.</div>
      <div class="btn">Patient Chart</div>
    </div>
  </main>

  <footer class="footer">©2018 Halvyne.<span>|</span>Help<span>|</span>Contact Us</footer>
</div>
</body>
</html>
```